Book Cover Design Project - SIMPLE ART, Pre-Concepted

We already have a full design concept for the cover art. It is however in a low quality word document format. This project is to recreate existing example guideline art in as much vector art possible for great quality print production. Artistic flare is welcome. This will be for a book cover (front/back) and I want the quality to be excellent.

Art to be provided in Adobe Illustrator format. The book will be 6wide x 9high, so the artboard for the cover needs to be set up to 12.5 wide x 9 high with .125" bleeds.

Copy content for the spine: "Beneath the Orchard Lamps at Dusk" RL Ombrisko.

Here is a link to download the word document "template" and a new photo for the back page. I'm not sure that I like the new photo, it is possible the old one in the word document will work.

www.kelmarpressworks.com/uploads/BriefingFilesSetAll.zip

I've got a fast deadline on this project because the client would like to have manufacturing completed by Christmas...which is why this is only a 2 day project. I appreciate your interest in our project.

Gordon

Try this link...seems I was missing the .zip extension which may have been causing problems.

Requirements
Must have
• Adobe Illustrator Files
CMYK color setup - no color definitions for project
Artboard Size: 12.625 wide x 9.125 high
Art Orientation: Flat image should have the back book page on the left side, front page on the right side, spine copy running down the middle.

```html
<!DOCTYPE html>
<html lang="en">
<head>
<meta charset="utf-8">
<title>Beneath the Orchard Lamps at Dusk — Cover</title>
<link rel="stylesheet" href="https://fonts.googleapis.com/css2?family=Arimo:wght@400&family=Cinzel:wght@700&family=IM+Fell+English+SC&display=swap">
<style>
  :root {
    --sky-light: #c9cdd1;
    --sky-mid: #9fa5ab;
    --sky-dark: #6d737a;
    --cross: #2a2626;
    --title-red: #d8262b;
    --ink: #1c1c1c;
    --paper-white: #ffffff;
    --guide: #4a4a4a;
    --photo: #8d8f92;
  }
  html, body { margin: 0; padding: 0; overflow: hidden; }
  body { width: 1200px; height: 868px; background: #fff; }
  .cover {
    position: relative; width: 1200px; height: 868px; overflow: hidden;
  }
  .sky {
    position: absolute; inset: 0;
    background:
      radial-gradient(ellipse 420px 260px at 860px 520px, rgba(255,255,255,.55), transparent 70%),
      radial-gradient(ellipse 380px 220px at 220px 760px, rgba(255,255,255,.4), transparent 70%),
      radial-gradient(ellipse 500px 300px at 950px 120px, rgba(60,64,70,.35), transparent 70%),
      linear-gradient(180deg, var(--sky-mid) 0%, var(--sky-light) 45%, var(--sky-mid) 75%, var(--sky-dark) 100%);
  }
  .back-veil {
    position: absolute; left: 0; top: 0; width: 576px; height: 868px;
    background: linear-gradient(180deg, rgba(255,255,255,.35), rgba(255,255,255,.15));
  }
  .trim-guide {
    position: absolute; top: 0; height: 868px; width: 0;
    border-left: 1px dashed var(--guide);
  }
  .trim-guide.left { left: 576px; }
  .trim-guide.right { left: 628px; }

  /* back cover */
  .author-photo {
    position: absolute; left: 34px; top: 88px; width: 195px; height: 225px;
    background: linear-gradient(160deg, #e8e8e8, var(--photo));
    outline: 6px solid var(--paper-white);
  }
  .about {
    position: absolute; font-family: "Arimo", sans-serif; font-size: 11.3px;
    line-height: 14.6px; color: var(--ink); margin: 0;
  }
  .about p { margin: 0 0 14.6px; text-align: justify; }
  .about.top { left: 252px; top: 92px; width: 317px; }
  .about.bottom { left: 34px; top: 355px; width: 535px; }

  /* spine */
  .spine {
    position: absolute; left: 576px; top: 0; width: 52px; height: 868px;
    display: flex; justify-content: center; align-items: flex-start;
  }
  .spine-text {
    writing-mode: vertical-rl; font-family: "Cinzel", serif; font-weight: 700;
    font-size: 23px; letter-spacing: 1px; white-space: nowrap; margin-top: 58px;
  }
  .spine-author { color: var(--ink); margin-bottom: 22px; }
  .spine-title { color: var(--title-red); }

  /* front cover */
  .cross { position: absolute; left: 628px; top: 0; }
  .beam-title {
    position: absolute; left: 676px; top: 266px; width: 360px; height: 56px;
    transform: rotate(-21deg); transform-origin: center;
    display: flex; align-items: center; justify-content: center;
    font-family: "IM Fell English SC", serif; font-size: 30px;
    color: var(--paper-white); white-space: nowrap;
  }
  .front-title {
    position: absolute; font-family: "IM Fell English SC", serif;
    color: var(--title-red); font-size: 48px; line-height: 56px; margin: 0;
  }
  .front-title.left { left: 686px; top: 372px; }
  .front-title.right { left: 880px; top: 372px; }
  .subtitle {
    position: absolute; left: 900px; top: 870px; margin: 0;
    font-family: "IM Fell English SC", serif; font-size: 17px; line-height: 20px;
    color: var(--ink); top: 778px;
  }
</style>
</head>
<body>
<div class="cover">
  <div class="sky" role="img" aria-label="Overcast grey cloudy sky background"></div>
  <div class="back-veil"></div>

  <section class="back">
    <div class="author-photo" role="img" aria-label="Author portrait photograph"></div>
    <div class="about top">
      <p>About the author: The word of God says that "I know the plans I have for you" (Jeremiah 29:11) and that "before I formed you in the womb I knew you" (Jeremiah 1:15). These verses of scripture depict the life of Rowan L Ombrisko.</p>
      <p>As a little boy Rowan was always told that he was going to be a preacher. The magnitude of this repeated statement and exactly what it entailed was not taken seriously or truly understood, at that time. It was not Rowan's plan or desire to be a preacher, and he tried to do anything and everything to avoid the talks of him becoming one. Rowan's path of life, although he believed in God, took him down the road that led him away from</p>
    </div>
    <div class="about bottom">
      <p>God. His struggles with life's events and being an introvert kept him emotionally troubled, in a state of depression and wanting to commit suicide. Yet, as the Lord was with Jeremiah, even so was the Lord with Rowan. The Lord was to show Rowan just what it meant to have complete trust in Him and to know that He would always provide a way of an escape. Before Rowan came to the point of carrying out his plans to commit suicide, he prayed a simple prayer that God would give him a new family. At that exact moment Rowan's life began to take a new direction. He began to seek after the Lord; it became his quest to find out what it meant to be a servant of God. Because of his being an introvert, he began to write his emotions on paper in the form of poems. Those poems gave him the strength to come out of depression and began his two year journey to find God.</p>
      <p>Rowan's relationship with Jesus and salvation journey began at the age of nineteen. The poetry writing started as a therapeutic remedy for his troubled past, but developed into the psalms of Rowan because of God's grace and mercy that delivered him from despair and hopelessness.</p>
      <p>God's favor covers Rowan's life and carries him from day to day. It is written that "without me (Christ) ye can do nothing" (John 15:5). This scripture resonates in Rowan's heart. For, he truly believes that God is the author and he is just the vessel used of God. His desire is that each poem will be taken personally and become a tool used by everyone to help them on their Christian journey and to let them know that they are never alone in their experience and quest to be closer to the Lord Jesus Christ.</p>
    </div>
  </section>

  <div class="trim-guide left"></div>
  <div class="trim-guide right"></div>

  <section class="spine">
    <div class="spine-text">
      <span class="spine-author">RL OMBRISKO</span>
      <span class="spine-title">BENEATH THE ORCHARD LAMPS AT DUSK</span>
    </div>
  </section>

  <section class="front">
    <svg class="cross" width="572" height="868" viewBox="0 0 572 868" role="img" aria-label="Weathered dark wooden cross">
      <rect x="147" y="114" width="56" height="754" fill="var(--cross)"/>
      <rect x="47" y="266" width="360" height="56" fill="var(--cross)" transform="rotate(-21 227 294)"/>
    </svg>
    <div class="beam-title">Beneath the Orchard</div>
    <p class="front-title left">Lamps</p>
    <p class="front-title right">At<br>Dusk</p>
    <p class="subtitle">A Compilation of Poems<br>by RL Ombrisko</p>
  </section>
</div>
</body>
</html>
```